International Petrochemical business needs a web design for Tessaro Desk system

We need a web design for a "Tessaro Desk" system for an international petrochemical company. The web site is used internally within the company. It is hosted by an internal department which provides government permit request service for other departments.

We would like to see designs of two pages using color light blue. (home page, internal page as attached).
Home Page:
1. Header has a background image and small animation. Header on home page can be taller than the header of the internal page.
2. Layout as attached.

Internal Page:
1. Header can use the same background image as the home page and can be shorter to utilize the page for content.
2. The blue icon behind every captions represent an icon. When user move mouse over this icon, it displays the caption in Thai language as a tooltip. This icon needs to be redesign.

The final design should communicate the followings:
- Excellent service provided system in terms of time and accurary
- Rapid growth of business via building petrochemical refinery plant

For Internal Page, the blue circle behind every captions represent an icon. When mouse over this icon, a tool tip showing the caption in Thai language is shown. Please also design this icon..

There are more feedbacks from customer as followed:

1. Banner should consists of 
    1.1 "Approved" stamp on paper
    1.2 An image of Garuda. It is used on every government documents in Thailand
    1.3 Image of petrochemical plant
2. Each menu item (Home, Permit, Search, etc) should have different colors. Drop down menu will use the same color as its parent menu item.
3. Overall tone of the web page should be light blue with background of the body the web page in white
4. "New Request" button should use green color with icon on it
5. Table header of each box in the body of the page should use dark blue background with text in white

Please kindly submit your revisions.
Thank you.

Reason: We get some late feedbacks from customers which was just updated to all designers.

• 1. Design for 1024x768 screen resolution
2. Use light blue theme
3. Background of header where the company logo is must have white background

```html
<!DOCTYPE html>
<html lang="en">
<head>
<meta charset="utf-8">
<title>Tessaro Desk – Home</title>
<link href="https://fonts.googleapis.com/css2?family=PT+Sans:wght@400;700&display=swap" rel="stylesheet">
<style>
  :root {
    --blue: #0a9ee0;
    --blue-light: #2cc0f5;
    --blue-dark: #0788c8;
    --text: #666;
    --text-soft: #8a8a8a;
    --line: #d8d8d8;
    --panel-head: #f4f4f4;
    --row-odd: #efefef;
    --row-even: #f8f8f8;
    --footer: #eeeeee;
    --white: #fff;
  }
  * { box-sizing: border-box; margin: 0; padding: 0; }
  html, body { width: 1200px; height: 855px; overflow: hidden; background: var(--white); }
  body { position: relative; font-family: "PT Sans", sans-serif; color: var(--text); font-size: 9.5px; }

  .brand { position: absolute; left: 181px; top: 22px; display: flex; align-items: center; gap: 6px; }
  .brand-mark { width: 26px; height: 26px; border-radius: 50%; background: var(--blue); }
  .brand-name { font-size: 12px; font-weight: 700; color: var(--blue); line-height: 1.05; text-transform: uppercase; }

  .main-nav { position: absolute; left: 181px; top: 69px; width: 846px; height: 29px; border-radius: 3px;
    background: linear-gradient(#34c6f7, #0aa2e4); }
  .main-nav a { position: absolute; top: 0; height: 29px; line-height: 29px; color: var(--white);
    text-decoration: none; font-size: 9.5px; transform: translateX(-50%); text-transform: uppercase; }
  .main-nav a.active { top: 5px; height: 18px; line-height: 18px; width: 58px; text-align: center;
    background: var(--white); color: var(--blue); border-radius: 2px; }

  .dropdown { position: absolute; left: 267px; top: 100px; width: 127px; height: 72px; background: var(--white);
    border: 1px solid var(--line); z-index: 2; padding: 0 7px; }
  .dropdown a { display: block; height: 23px; line-height: 23px; color: var(--text-soft); font-size: 8px;
    text-decoration: none; border-bottom: 1px solid #e4e4e4; padding-left: 6px; }
  .dropdown a:last-child { border-bottom: 0; }

  .hero { position: absolute; left: 181px; top: 104px; width: 846px; height: 143px; border-radius: 4px;
    background: linear-gradient(90deg, #5b4a7a 0%, #2e2a45 35%, #222 60%, #000 85%); overflow: hidden; }
  .hero-plant { position: absolute; left: 0; right: 0; bottom: 0; height: 60px;
    background: linear-gradient(180deg, rgba(180,170,220,.25), rgba(140,60,150,.55)); }
  .hero-title { position: absolute; left: 636px; top: 57px; color: var(--white); font-size: 15.5px; line-height: 20px; text-transform: uppercase; }
  .hero-dots { position: absolute; left: 796px; top: 122px; display: flex; gap: 3px; }
  .hero-dots span { width: 7px; height: 7px; background: #555; }
  .hero-dots span:first-child { background: var(--blue); }

  .panel { position: absolute; border: 1px solid var(--line); border-radius: 2px; background: var(--white); }
  .panel-head { height: 28px; line-height: 28px; padding-left: 12px; background: var(--panel-head);
    border-bottom: 1px solid var(--line); color: var(--blue); font-weight: 700; font-size: 9.5px; text-transform: uppercase; }
  .data-table { position: absolute; left: 11px; right: 11px; top: 34px; }
  .data-row { display: grid; grid-template-columns: var(--cols); height: 20px; line-height: 20px; padding-left: 10px; }
  .data-row.labels { color: var(--blue); margin-bottom: 4px; text-transform: uppercase; }
  .data-row.item { color: var(--text); border-bottom: 1px solid #e2e2e2; }
  .data-row.item:nth-of-type(even) { background: var(--row-odd); }
  .data-row.item:nth-of-type(odd) { background: var(--row-even); }
  .heart { width: 9px; height: 8px; vertical-align: -1px; margin-left: 4px; fill: var(--blue); }

  .pager { position: absolute; left: 10px; bottom: 9px; display: flex; gap: 4px; align-items: center; color: var(--text-soft); font-size: 8px; }
  .pager span.page { width: 13px; height: 13px; line-height: 11px; text-align: center; border: 1px solid #c9c9c9; border-radius: 2px; background: #f2f2f2; }

  .new-request { position: absolute; left: 612px; top: 574px; width: 415px; height: 41px; border-radius: 3px;
    background: linear-gradient(#2ec2f6, #0a9ee0); }
  .new-request h2 { position: absolute; left: 19px; top: 0; line-height: 41px; color: var(--white); font-weight: 400; font-size: 18px; letter-spacing: .3px; text-transform: uppercase; }
  .new-request a { position: absolute; right: 9px; top: 8px; width: 85px; height: 24px; line-height: 24px; text-align: center;
    background: var(--white); color: var(--blue); text-decoration: none; font-size: 11px; border-radius: 2px; text-transform: uppercase; }

  .site-footer { position: absolute; left: 181px; top: 789px; width: 846px; height: 35px; background: var(--footer); border-radius: 2px; }
  .footer-nav { position: absolute; left: 20px; top: 0; line-height: 35px; font-size: 8px; color: var(--text-soft); text-transform: uppercase; }
  .footer-nav span.sep { margin: 0 12px; }
  .copyright { position: absolute; right: 20px; top: 0; line-height: 35px; font-size: 8px; color: var(--text-soft); text-transform: uppercase; }
</style>
</head>
<body>
  <div class="brand">
    <span class="brand-mark"></span>
    <span class="brand-name">Norvale<br>Petrochemical</span>
  </div>

  <nav class="main-nav">
    <a href="#" style="left:38px">Home</a>
    <a href="#" class="active" style="left:115px">Permits</a>
    <a href="#" style="left:194px">Search</a>
    <a href="#" style="left:271px">Report</a>
    <a href="#" style="left:347px">Admin</a>
    <a href="#" style="left:418px">Help</a>
  </nav>
  <div class="dropdown">
    <a href="#">CREATE NEW PERMIT</a>
    <a href="#">TRANSFER ROLE</a>
    <a href="#">TRANSFER RES. PERSON</a>
  </div>

  <header class="hero">
    <div class="hero-plant" role="img" aria-label="Petrochemical refinery plant lit at night"></div>
    <p class="hero-title">Online system for<br>petrochemical company</p>
    <div class="hero-dots"><span></span><span></span><span></span><span></span></div>
  </header>

  <section class="panel" style="left:181px; top:261px; width:415px; height:165px;">
    <div class="panel-head">New Requests</div>
    <div class="data-table" style="--cols:155px 176px 1fr">
      <div class="data-row labels"><span>Request No.</span><span>Requested Date</span><span>Branch</span></div>
      <div class="data-row item"><span>56-0003</span><span>&nbsp;&nbsp;&nbsp;20/4/2013</span><span>&nbsp;GC1</span></div>
      <div class="data-row item"><span>56-0004</span><span>&nbsp;&nbsp;&nbsp;20/4/2014</span><span>&nbsp;GC2</span></div>
    </div>
    <div class="pager">&lsaquo;<span class="page">1</span><span class="page">2</span><span class="page">3</span><span class="page">4</span>&rsaquo;</div>
  </section>

  <section class="panel" style="left:612px; top:261px; width:415px; height:165px;">
    <div class="panel-head">My Working Requests</div>
    <div class="data-table" style="--cols:112px 124px 1fr">
      <div class="data-row labels"><span>Request No.</span><span>Requested Date</span><span>Status</span></div>
      <div class="data-row item"><span>55-0200</span><span>&nbsp;&nbsp;&nbsp;25/3/2013</span><span>Waiting for process</span></div>
      <div class="data-row item"><span>55-0210</span><span>&nbsp;&nbsp;&nbsp;24/3/2013</span><span>In progress</span></div>
      <div class="data-row item"><span>55-0300</span><span>&nbsp;&nbsp;&nbsp;18/1/2013</span><span>Incomplete document</span></div>
      <div class="data-row item"><span>55-0301</span><span>&nbsp;&nbsp;&nbsp;18/1/2013</span><span>Cancel requested</span></div>
    </div>
    <div class="pager">&lsaquo;<span class="page">1</span><span class="page">2</span><span class="page">3</span><span class="page">4</span>&rsaquo;</div>
  </section>

  <section class="panel" style="left:181px; top:436px; width:846px; height:129px;">
    <div class="panel-head">Expiring Permits</div>
    <div class="data-table" style="--cols:155px 142px 155px 101px 147px 1fr">
      <div class="data-row labels"><span>Permit No</span><span>Expire Date</span><span>Permit Name</span><span>Branch</span><span>Required Time (Day)</span><span>Due Date</span></div>
      <div class="data-row item"><span>56-0003</span><span>&nbsp;20/4/2013</span><span>Permit Name ###10</span><span>&nbsp;GC1</span><span>&nbsp;&nbsp;&nbsp;&nbsp;&nbsp;&nbsp;&nbsp;&nbsp;30<svg class="heart" viewBox="0 0 10 9"><path d="M5 9 0.8 4.6A2.4 2.4 0 0 1 5 1.4 2.4 2.4 0 0 1 9.2 4.6Z"/></svg></span><span>&nbsp;&nbsp;&nbsp;-40</span></div>
      <div class="data-row item"><span>56-0004</span><span>&nbsp;20/4/2014</span><span>Permit Name ###20</span><span>&nbsp;GC2</span><span>&nbsp;&nbsp;&nbsp;&nbsp;&nbsp;&nbsp;&nbsp;&nbsp;60<svg class="heart" viewBox="0 0 10 9"><path d="M5 9 0.8 4.6A2.4 2.4 0 0 1 5 1.4 2.4 2.4 0 0 1 9.2 4.6Z"/></svg></span><span>&nbsp;&nbsp;&nbsp;15</span></div>
    </div>
    <div class="pager">&lsaquo;<span class="page">1</span><span class="page">2</span><span class="page">3</span><span class="page">4</span>&rsaquo;</div>
  </section>

  <section class="panel" style="left:181px; top:574px; width:415px; height:198px;">
    <div class="panel-head">My In Progress Requests</div>
    <div class="data-table" style="--cols:131px 140px 1fr">
      <div class="data-row labels"><span>Request No.</span><span>Requested Date</span><span>Status</span></div>
      <div class="data-row item"><span>56-0003</span><span>&nbsp;&nbsp;&nbsp;20/4/2013</span><span>Incomplete document</span></div>
      <div class="data-row item"><span>56-0004</span><span>&nbsp;&nbsp;&nbsp;20/4/2014</span><span>Incomplete document</span></div>
    </div>
    <div class="pager">&lsaquo;<span class="page">1</span><span class="page">2</span><span class="page">3</span><span class="page">4</span>&rsaquo;</div>
  </section>

  <div class="new-request">
    <h2>New Request</h2>
    <a href="#">Click here</a>
  </div>

  <section class="panel" style="left:612px; top:624px; width:415px; height:148px;">
    <div class="panel-head">Recent Completed Requests</div>
    <div class="data-table" style="--cols:112px 1fr">
      <div class="data-row labels"><span>Request No.</span><span>Completed Date</span></div>
      <div class="data-row item"><span>55-0200</span><span>&nbsp;25/3/2013</span></div>
      <div class="data-row item"><span>55-0210</span><span>&nbsp;24/3/2013</span></div>
      <div class="data-row item"><span>55-0300</span><span>&nbsp;18/1/2013</span></div>
    </div>
    <div class="pager">&lsaquo;<span class="page">1</span><span class="page">2</span><span class="page">3</span><span class="page">4</span>&rsaquo;</div>
  </section>

  <footer class="site-footer">
    <div class="footer-nav">Home<span class="sep">|</span>Permits<span class="sep">|</span>Search<span class="sep">|</span>Report<span class="sep">|</span>Admin<span class="sep">|</span>Help</div>
    <div class="copyright">Copyright © 2013 Norvale Petrochemical. All rights reserved.</div>
  </footer>
</body>
</html>
```